ALL ASPECTS OF PLASTERING INC: TEXTURE,SANDFINISH RENO,POOLS, PATCH WORK ( STATEWIDE SERVICE GOOD RATES) 100% GUARANTEED FULLY INSURED C

Target Market(s)

ANYONE WHO OWNS A HOUSE,BUILDERS

Industry/Entity Type

Work

Contact Information for Business Card

GRITT-WALL PLASTERING SERVICES
BERNARD KOVALEC 0438259164
EMAIL:TARVEK48@QUILLMAIL.COM

Requirements
Must have
• COLOUR BACKGROUND WIV PLASTERING PICTURE EG TROWEL, CEMENT MIXER, SAND
Nice to have
• BOLD PROFESSIONAL LOOKING AND SOUNDING CATCHY SAYING
Should not have
• FLURO COLOURS

```html
<!DOCTYPE html>
<html lang="en">
<head>
<meta charset="UTF-8">
<title>Gritt-Wall Plastering Services – Business Card</title>
<link rel="stylesheet" href="https://fonts.googleapis.com/css2?family=Jost:wght@400;500&display=swap">
<style>
  :root {
    --backdrop: #f6c290;
    --card: #9b5148;
    --card-light: #a4594f;
    --text: #ffffff;
    --rule: #f2c200;
  }
  * { margin: 0; padding: 0; box-sizing: border-box; }
  html, body {
    width: 1200px;
    height: 541px;
    overflow: hidden;
    background: var(--backdrop);
    font-family: "Jost", "Futura", sans-serif;
    color: var(--text);
  }
  .canvas {
    position: relative;
    width: 1200px;
    height: 541px;
  }
  .card {
    position: absolute;
    top: 104px;
    width: 538px;
    height: 315px;
    border-radius: 14px;
    background: linear-gradient(160deg, var(--card-light), var(--card));
  }
  .card--front { left: 35px; }
  .card--back { left: 611px; }

  .owner-name {
    position: absolute;
    left: 28px;
    top: 44px;
    font-size: 19px;
    font-weight: 400;
  }
  .business-name {
    position: absolute;
    left: 27px;
    top: 116px;
    font-size: 54px;
    font-weight: 400;
    line-height: 1;
    letter-spacing: 0.5px;
  }
  .business-type {
    position: absolute;
    left: 28px;
    top: 174px;
    font-size: 26px;
    font-weight: 400;
    line-height: 1;
  }
  .rule {
    position: absolute;
    left: 28px;
    top: 211px;
    width: 486px;
    height: 3px;
    background: var(--rule);
  }
  .contact {
    position: absolute;
    left: 298px;
    top: 252px;
    font-size: 14px;
    line-height: 18px;
    list-style: none;
    letter-spacing: 0.3px;
  }

  .services {
    position: absolute;
    left: 0;
    right: 0;
    top: 110px;
    text-align: center;
    font-size: 18px;
    line-height: 23px;
    font-weight: 400;
  }
  .services .guarantee { margin-top: 4px; }
</style>
</head>
<body>
  <main class="canvas">
    <section class="card card--front" aria-label="Business card front">
      <p class="owner-name">Bernard Kovalec</p>
      <h1 class="business-name">GRITT-WALL</h1>
      <p class="business-type">PLASTERING SERVICES</p>
      <div class="rule"></div>
      <ul class="contact">
        <li>T : 0438259164</li>
        <li>E : tarvek48@quillmail.com</li>
      </ul>
    </section>

    <section class="card card--back" aria-label="Business card back">
      <div class="services">
        <p>All Aspects Of Plastering Inc:</p>
        <p>Texture, Sandfinish Reno, Pools, Patch Work</p>
        <p>(Statewide Service Good Rates)</p>
        <p class="guarantee">100% Guaranteed Fully Insured C</p>
      </div>
    </section>
  </main>
</body>
</html>
```